New corporate PowerPoint template

We need a new corporate presentation template. A master slide and also some suggestions.
See our attached file with some ideas.
We want it to be clean, professional, innovative and impressive. Have it match our new website design. The presentation should be able to communicate our message and products clearly.
We need a new template that can be used both internally and in customer-presentations.
Target Market(s)
CFOs, CTOs, Controllers, Leaders, Managers.
Industry/Entity Type
Information Technology
Colors
Designer to choose colors to be used in the design.
Requirements
Must have
- - Master slide so that the template can be used in the organization
- - logo
- - clean design
- - easy to use in the future
- - see file for detailed info
- - place some of the attached solutions in screens.
- The master slide should contain structure for and the following slides:
- - distances
- - a few sample slides
- - charts and graphs - designs and predefined charts and graphs, so that the users of the PowerPoint template need to do nothing else but to enter their data.
- - title page
- - Agenda page - what is the presentation going to cover, not in a bullet point list
- - bar chart page
- - Text only page
- - Text with graphic
- Image & video - slides that have just a placeholder for eighter a high-quality photo or video
- - About me or team slide (usually1 - 5)
- - a table page
- - timelines
- - Other slides that we need(?) Please add other frequently-used slides that you think we need
- - closing slide
- - The master can contain several layouts
- - color palette / organized in a good way / use our brand colors
- - fonts: Arial (Montserrat is our main font - but users must be able to use Arial if the want to)

```html
<!DOCTYPE html>
<html lang="en">
<head>
<meta charset="utf-8">
<title>Tallyforge presentation template</title>
<link href="https://fonts.googleapis.com/css2?family=Open+Sans:wght@400;600;700;800&display=swap" rel="stylesheet">
<style>
:root{
  --page:#e9ecef;
  --navy:#0c2547;
  --navy-2:#133a6b;
  --blue:#1f5fa6;
  --sky:#3d93d6;
  --ice:#dbe8f4;
  --orange:#f07a24;
  --ink:#1b2a3d;
  --grey:#8a94a0;
  --line:#d3d9e0;
  --white:#ffffff;
}
*{box-sizing:border-box;margin:0;padding:0}
html,body{width:776px;height:1200px;overflow:hidden;background:var(--page);font-family:"Open Sans",Arial,sans-serif;color:var(--ink)}
.deck{display:grid;grid-template-columns:repeat(3,245px);grid-auto-rows:138px;gap:9px 9px;padding:16px 11px;}
.slide{position:relative;overflow:hidden;background:var(--white);box-shadow:0 1px 3px rgba(0,0,0,.18)}
.abs{position:absolute}
.photo{position:absolute}
.title{position:absolute;left:12px;top:10px;font-weight:700;font-size:9px;color:var(--navy)}
.title.center{left:0;right:0;text-align:center}
.txt{position:absolute;font-size:4px;line-height:6px;color:var(--grey)}
.bar{position:absolute;height:3px;background:var(--line);border-radius:1px}
.foot{position:absolute;left:0;right:0;bottom:0;height:4px;background:linear-gradient(90deg,var(--navy),var(--sky))}
.brand{font-weight:800;color:var(--white);letter-spacing:-.3px}
.btn{position:absolute;background:var(--orange);color:var(--white);font-size:4px;font-weight:700;padding:2px 6px;border-radius:6px}
.screen{position:absolute;background:var(--navy);border-radius:3px;padding:3px}
.screen .inner{width:100%;height:100%;background:linear-gradient(180deg,#f4f7fa,#dce6f0)}
.blue-bg{background:linear-gradient(135deg,var(--navy) 0%,var(--blue) 100%)}
.white{color:var(--white)}
</style>
</head>
<body>
<main class="deck">

<!-- 1 title with device -->
<section class="slide blue-bg">
  <div class="photo" role="img" aria-label="Laptop showing dashboard software" style="left:40px;top:8px;width:165px;height:100px;background:linear-gradient(180deg,#d7e3ef,#8fb0cf);border-radius:4px"></div>
  <div class="abs" style="left:0;right:0;bottom:0;height:30px;background:var(--navy)"></div>
  <div class="bar" style="left:60px;bottom:14px;width:125px;background:#4b6a92"></div>
</section>

<!-- 2 title with device and button -->
<section class="slide blue-bg">
  <div class="photo" role="img" aria-label="Laptop showing dashboard software" style="left:40px;top:8px;width:165px;height:100px;background:linear-gradient(180deg,#d7e3ef,#8fb0cf);border-radius:4px"></div>
  <div class="abs" style="left:0;right:0;bottom:0;height:30px;background:var(--navy)"></div>
  <div class="btn" style="right:18px;bottom:10px">Get started</div>
</section>

<!-- 3 brand title -->
<section class="slide" style="background:linear-gradient(160deg,var(--navy-2),var(--navy))">
  <div class="abs brand" style="left:0;right:0;top:36px;text-align:center;font-size:26px">tallyforge</div>
  <div class="abs white" style="left:0;right:0;top:74px;text-align:center;font-size:5px">Planning, budgeting and reporting for finance teams</div>
  <div class="abs" style="left:50px;right:50px;top:84px;height:8px;background:var(--orange);color:#fff;font-size:4px;font-weight:700;text-align:center;line-height:8px">SMARTER DECISIONS, FASTER</div>
</section>

<!-- 4 city photo title -->
<section class="slide" style="background:var(--navy)">
  <div class="photo" role="img" aria-label="City skyline at night" style="inset:0;background:linear-gradient(180deg,#0f2d55 0%,#1c4f86 60%,#0a1e3a 100%)"></div>
  <div class="abs brand" style="left:16px;top:40px;font-size:20px">tallyforge</div>
  <div class="abs white" style="left:16px;top:68px;font-size:5px">Presentation subtitle here</div>
</section>

<!-- 5 quote bubble -->
<section class="slide" style="background:linear-gradient(180deg,#fff 0 55%,var(--blue) 55%)">
  <div class="abs" style="left:50px;top:18px;width:145px;height:66px;background:#fff;border-radius:8px;box-shadow:0 1px 4px rgba(0,0,0,.25)"></div>
  <svg class="abs" style="left:110px;top:82px" width="14" height="10"><path d="M0 0h14L7 10z" fill="#fff"/></svg>
  <div class="txt" style="left:62px;top:34px;width:122px;text-align:center;color:var(--ink)">“Our finance team closes the month in half the time and trusts every number it reports.”</div>
  <div class="foot"></div>
</section>

<!-- 6 history -->
<section class="slide">
  <div class="abs" style="left:88px;top:0;width:22px;bottom:0;background:var(--blue)"></div>
  <div class="abs white" style="left:92px;top:80px;font-size:8px;font-weight:700;transform:rotate(-90deg);transform-origin:left top;">History</div>
  <div class="photo" role="img" aria-label="Hands typing on a laptop" style="left:112px;top:20px;width:70px;height:70px;background:linear-gradient(135deg,#c9d6e2,#6f8aa5)"></div>
  <div class="txt" style="left:188px;top:22px;width:52px">Founded in 1998, the company grew from a small team into a leading provider of finance software.</div>
  <div class="txt" style="left:10px;top:20px;width:72px">Short notes on key years and milestones of the journey so far.</div>
</section>

<!-- 7 screen with table -->
<section class="slide">
  <div class="title">Lorem ipsum dolor sit amet</div>
  <div class="screen" style="left:12px;top:28px;width:120px;height:78px"><div class="inner"></div></div>
  <div class="txt" style="left:145px;top:34px;width:88px">Use this layout to present a product screen with a short description beside it.</div>
  <div class="foot"></div>
</section>

<!-- 8 picture and text -->
<section class="slide">
  <div class="abs" style="left:0;top:0;width:100px;bottom:0;background:var(--ice)"></div>
  <div class="abs" style="left:12px;top:30px;font-size:6px;font-weight:700;color:var(--navy)">PICTURE AND TEXT</div>
  <div class="txt" style="left:12px;top:42px;width:80px">Describe the picture and its message in two or three short lines.</div>
  <div class="screen" style="left:110px;top:24px;width:120px;height:80px;transform:skewX(-6deg)"><div class="inner"></div></div>
  <div class="foot"></div>
</section>

<!-- 9 page break -->
<section class="slide blue-bg">
  <div class="photo" role="img" aria-label="Person working on a laptop" style="left:0;top:0;width:110px;bottom:0;background:linear-gradient(135deg,#5f7e9e,#1d3c62)"></div>
  <div class="abs white" style="left:125px;top:58px;font-size:13px;font-weight:700">Page break</div>
</section>

<!-- 10 text columns -->
<section class="slide">
  <div class="title">Lorem ipsum dolor sit amet</div>
  <div class="bar" style="left:12px;top:34px;width:64px;background:var(--sky)"></div>
  <div class="bar" style="left:90px;top:34px;width:64px;background:var(--sky)"></div>
  <div class="bar" style="left:168px;top:34px;width:64px;background:var(--sky)"></div>
  <div class="txt" style="left:12px;top:42px;width:64px">Text only layout for longer points, split into three balanced columns.</div>
  <div class="txt" style="left:90px;top:42px;width:64px">Keep each column short and focused on a single idea.</div>
  <div class="txt" style="left:168px;top:42px;width:64px">Close with the key result or next step for readers.</div>
  <div class="foot"></div>
</section>

<!-- 11 timeline -->
<section class="slide">
  <div class="title center">Timeline</div>
  <div class="abs" style="left:18px;right:18px;top:68px;height:2px;background:var(--line)"></div>
  <svg class="abs" style="left:18px;top:60px" width="210" height="18">
    <circle cx="10" cy="9" r="6" fill="#1f5fa6"/><circle cx="72" cy="9" r="6" fill="#3d93d6"/>
    <circle cx="138" cy="9" r="6" fill="#1f5fa6"/><circle cx="200" cy="9" r="6" fill="#f07a24"/>
  </svg>
  <div class="txt" style="left:14px;top:84px;width:40px">2019 Launch</div>
  <div class="txt" style="left:76px;top:84px;width:40px">2020 Growth</div>
  <div class="txt" style="left:142px;top:84px;width:40px">2022 Cloud</div>
  <div class="txt" style="left:200px;top:84px;width:40px">2024 Today</div>
  <div class="foot"></div>
</section>

<!-- 12 two factors donut -->
<section class="slide">
  <div class="title">Two factors &amp; conclusion</div>
  <div class="abs" style="left:12px;top:34px;width:90px;height:22px;background:var(--blue)"></div>
  <div class="abs" style="left:12px;top:62px;width:90px;height:22px;background:var(--sky)"></div>
  <svg class="abs" style="left:140px;top:30px" width="70" height="70" viewBox="0 0 70 70">
    <circle cx="35" cy="35" r="25" fill="none" stroke="#dbe8f4" stroke-width="12"/>
    <circle cx="35" cy="35" r="25" fill="none" stroke="#1f5fa6" stroke-width="12" stroke-dasharray="110 157" transform="rotate(-90 35 35)"/>
  </svg>
  <div class="txt" style="left:12px;top:92px;width:100px">Conclusion text goes here.</div>
  <div class="foot"></div>
</section>

<!-- 13 four factors -->
<section class="slide">
  <div class="title">Four factors &amp; conclusion</div>
  <svg class="abs" style="left:12px;top:34px" width="150" height="80">
    <path d="M0 0h60l10 9-10 9H0z" fill="#0c2547"/>
    <path d="M20 20h60l10 9-10 9H20z" fill="#133a6b"/>
    <path d="M40 40h60l10 9-10 9H40z" fill="#1f5fa6"/>
    <path d="M60 60h60l10 9-10 9H60z" fill="#3d93d6"/>
  </svg>
  <div class="txt" style="left:170px;top:40px;width:68px">Each step builds on the one before and leads to the conclusion.</div>
  <div class="foot"></div>
</section>

<!-- 14 six factors -->
<section class="slide">
  <div class="title center">Six factors &amp; conclusion</div>
  <svg class="abs" style="left:92px;top:30px" width="62" height="62" viewBox="0 0 62 62" fill="none" stroke-width="7">
    <path d="M31 6a25 25 0 0 1 21.6 12.5" stroke="#0c2547"/>
    <path d="M52.6 18.5a25 25 0 0 1 0 25" stroke="#1f5fa6"/>
    <path d="M52.6 43.5A25 25 0 0 1 31 56" stroke="#3d93d6"/>
    <path d="M31 56a25 25 0 0 1-21.6-12.5" stroke="#f07a24"/>
    <path d="M9.4 43.5a25 25 0 0 1 0-25" stroke="#133a6b"/>
    <path d="M9.4 18.5A25 25 0 0 1 31 6" stroke="#3d93d6"/>
  </svg>
  <div class="txt" style="left:12px;top:36px;width:70px;text-align:right">Factor one<br><br>Factor two<br><br>Factor three</div>
  <div class="txt" style="left:164px;top:36px;width:70px">Factor four<br><br>Factor five<br><br>Factor six</div>
  <div class="foot"></div>
</section>

<!-- 15 headline with laptop -->
<section class="slide">
  <div class="title">Write your headline</div>
  <div class="txt" style="left:12px;top:30px;width:80px">Short supporting text that explains the product screen on the right.</div>
  <div class="screen" style="left:110px;top:30px;width:122px;height:76px"><div class="inner"></div></div>
  <div class="foot"></div>
</section>

<!-- 16 table & chart -->
<section class="slide blue-bg">
  <div class="abs white" style="left:12px;top:10px;font-size:12px;font-weight:700">Table &amp; Chart</div>
  <svg class="abs" style="left:12px;top:36px" width="120" height="80">
    <rect width="120" height="12" fill="#3d93d6"/>
    <g fill="#ffffff" opacity=".9"><rect y="16" width="120" height="10"/><rect y="30" width="120" height="10"/><rect y="44" width="120" height="10"/><rect y="58" width="120" height="10"/></g>
  </svg>
  <svg class="abs" style="left:150px;top:30px" width="80" height="80" viewBox="0 0 80 80">
    <circle cx="40" cy="40" r="36" fill="#dbe8f4"/>
    <path d="M40 40V4a36 36 0 0 1 34 48z" fill="#3d93d6"/>
    <path d="M40 40l34 12a36 36 0 0 1-30 23z" fill="#0c2547"/>
  </svg>
</section>

<!-- 17 four contents and quote -->
<section class="slide">
  <div class="title center">Four contents and a quote</div>
  <div class="abs" style="left:12px;right:12px;top:30px;height:34px;background:var(--ice)"></div>
  <div class="txt" style="left:20px;top:40px;width:205px;text-align:center;color:var(--navy)">“A short quote that frames the four topics below.”</div>
  <div class="txt" style="left:12px;top:76px;width:50px">Content one</div>
  <div class="txt" style="left:70px;top:76px;width:50px">Content two</div>
  <div class="txt" style="left:128px;top:76px;width:50px">Content three</div>
  <div class="txt" style="left:186px;top:76px;width:50px">Content four</div>
  <div class="foot"></div>
</section>

<!-- 18 person with text -->
<section class="slide">
  <div class="photo" role="img" aria-label="Team member standing in an office" style="left:0;top:0;width:105px;bottom:0;background:linear-gradient(180deg,#8aa3bc,#2c4a6e)"></div>
  <div class="abs" style="left:115px;top:14px;font-size:9px;font-weight:700;color:var(--navy);width:120px">Lorem ipsum dolor sit amet</div>
  <div class="txt" style="left:115px;top:44px;width:120px">Introduce a team member with role, background and contact.</div>
  <div class="foot"></div>
</section>

<!-- 19 big stat -->
<section class="slide">
  <div class="title">Lorem ipsum dolor sit amet</div>
  <svg class="abs" style="left:12px;top:30px" width="60" height="60"><circle cx="30" cy="30" r="26" fill="none" stroke="#1f5fa6" stroke-width="4"/></svg>
  <div class="abs" style="left:12px;top:50px;width:60px;text-align:center;font-size:11px;font-weight:800;color:var(--navy)">10 M</div>
  <div class="txt" style="left:82px;top:36px;width:150px">Key figure with a short note on what it means for the business.</div>
  <div class="foot"></div>
</section>

<!-- 20 bar chart -->
<section class="slide">
  <div class="title center">Lorem ipsum dolor sit amet</div>
  <div class="abs" style="left:20px;top:32px;width:120px;height:11px;background:var(--navy)"></div>
  <div class="abs" style="left:20px;top:50px;width:95px;height:11px;background:var(--orange)"></div>
  <div class="abs" style="left:20px;top:68px;width:140px;height:11px;background:var(--blue)"></div>
  <div class="abs" style="left:20px;top:86px;width:70px;height:11px;background:var(--sky)"></div>
  <div class="txt" style="left:170px;top:34px;width:66px">Sales 64%<br><br>Costs 48%<br><br>Growth 75%<br><br>Other 36%</div>
  <div class="foot"></div>
</section>

<!-- 21 icon list -->
<section class="slide">
  <div class="title">Lorem ipsum dolor sit amet</div>
  <div class="abs" style="left:12px;top:32px;width:14px;height:14px;background:var(--blue)"></div>
  <div class="abs" style="left:12px;top:54px;width:14px;height:14px;background:var(--sky)"></div>
  <div class="abs" style="left:12px;top:76px;width:14px;height:14px;background:var(--navy)"></div>
  <div class="txt" style="left:32px;top:34px;width:200px">First point with a short line of detail.</div>
  <div class="txt" style="left:32px;top:56px;width:200px">Second point with a short line of detail.</div>
  <div class="txt" style="left:32px;top:78px;width:200px">Third point with a short line of detail.</div>
  <div class="foot"></div>
</section>

<!-- 22 photo with text -->
<section class="slide">
  <div class="photo" role="img" aria-label="Bright office interior" style="inset:0;background:linear-gradient(135deg,#eef2f6,#b9c7d4)"></div>
  <div class="abs" style="left:14px;top:64px;font-size:9px;font-weight:700;color:var(--navy);width:110px">Lorem ipsum dolor sit amet</div>
  <div class="foot"></div>
</section>

<!-- 23 key features pyramid -->
<section class="slide">
  <div class="title center">Key Features Slide</div>
  <svg class="abs" style="left:88px;top:30px" width="70" height="80">
    <path d="M35 0L48 26H22z" fill="#3d93d6"/>
    <path d="M21 28h28l12 24H9z" fill="#1f5fa6"/>
    <path d="M8 54h54l8 24H0z" fill="#0c2547"/>
  </svg>
  <div class="txt" style="left:12px;top:40px;width:70px;text-align:right">Feature one<br><br><br>Feature two</div>
  <div class="txt" style="left:165px;top:40px;width:70px">Feature three<br><br><br>Feature four</div>
  <div class="foot"></div>
</section>

<!-- 24 magnifier stat -->
<section class="slide">
  <div class="title">Lorem ipsum dolor sit amet</div>
  <div class="txt" style="left:12px;top:32px;width:120px">Zoom in on one number that tells the main story of the deck.</div>
  <svg class="abs" style="left:150px;top:26px" width="86" height="100">
    <circle cx="38" cy="38" r="30" fill="#fff" stroke="#0c2547" stroke-width="6"/>
    <path d="M60 60l20 24" stroke="#0c2547" stroke-width="9" stroke-linecap="round"/>
  </svg>
  <div class="abs" style="left:158px;top:56px;width:60px;text-align:center;font-size:12px;font-weight:800;color:var(--blue)">10 M</div>
  <div class="foot"></div>
</section>

</main>
</body>
</html>
```